依頼詳細
参考資料として、以前社内で内製で作成したチラシを添付しています。
記載項目
添付内容参照ください。(Wordファイル/振袖スペシャルフェアのチラシ内容)
サイズ
A4
ページ数
両面
希望イメージ
シンプル 複雑
単色 カラフル
暗い 明るい
日常 高級
遊び心 厳粛
未来的 伝統的
女性的 男性的
希望する色
納品ファイル
• 高解像度JPG (.jpg)
• イラストレーター形式 (.ai)
補足説明
使用できる画像添付します。
https://48.kurobox.jp/0317-a7d41e92c5f08b3d6e1a9c70b2f58e31
■ 選んだ理由

弊館のイメージに一番近い形でのご提案でした。

■ 提案者全員のお礼・コメント

たくさんのご提案をいただきましてありがとうございました。

```html
<!DOCTYPE html>
<html lang="ja">
<head>
<meta charset="utf-8">
<title>振袖 special fair</title>
<link href="https://fonts.googleapis.com/css2?family=Noto+Serif+JP:wght@500;700&family=Noto+Sans+JP:wght@400;500;700&family=Montserrat:wght@300;400;500&display=swap" rel="stylesheet">
<style>
:root{
  --pink:#c9959a;
  --pink-deep:#b97d83;
  --pink-pale:#f3e4e4;
  --grey:#c4c2c2;
  --grey-soft:#eeeded;
  --ink:#5b5556;
  --white:#ffffff;
}
*{margin:0;padding:0;box-sizing:border-box}
html,body{width:846px;height:1200px;overflow:hidden;background:var(--white)}
body{font-family:"Noto Sans JP",sans-serif;color:var(--ink)}
.flyer{position:relative;width:846px;height:1200px;overflow:hidden;background:var(--white)}

.hero{position:absolute;left:0;top:0;width:846px;height:610px;background:var(--grey-soft)}
.hero-photo{position:absolute;left:270px;top:0;width:576px;height:610px;
  background:linear-gradient(160deg,#e7e3e2 0%,#d9cfcc 45%,#c9b3ad 75%,#e2d4cf 100%)}
.deco{position:absolute;background:var(--white)}
.deco.a{left:0;top:0;width:240px;height:90px;opacity:.55}
.deco.b{left:170px;top:300px;width:110px;height:90px;opacity:.6}

.collab{position:absolute;left:32px;top:30px;font-size:15px;letter-spacing:.12em;font-weight:500}

.kanji{position:absolute;width:114px;height:114px;background:var(--white);
  font-family:"Noto Serif JP",serif;font-weight:700;font-size:92px;line-height:114px;text-align:center;color:var(--pink-deep)}
.kanji.furi{left:56px;top:107px}
.kanji.sode{left:146px;top:205px;background:rgba(255,255,255,.85)}

.fair-title{position:absolute;left:56px;top:350px;font-family:"Montserrat",sans-serif;font-weight:300;
  font-size:50px;letter-spacing:.04em;color:var(--white)}

.date-band{position:absolute;left:0;top:440px;width:846px;height:58px;background:var(--pink);
  display:flex;align-items:center;padding-left:44px;color:var(--white)}
.date{font-family:"Montserrat",sans-serif;font-weight:500;font-size:40px;letter-spacing:.02em}
.day{display:inline-block;font-size:12px;background:var(--white);color:var(--pink);padding:1px 4px;margin:0 6px;vertical-align:middle}
.arrow{margin:0 14px;font-size:26px}
.times{position:absolute;left:544px;top:8px;font-size:24px;font-weight:500;letter-spacing:.04em}
.time-notes{position:absolute;left:554px;top:504px;display:flex;gap:22px}
.time-notes span{font-size:10px;background:var(--pink);color:var(--white);padding:1px 6px}

.points{position:absolute;left:0;top:610px;width:846px;height:390px;background:var(--white)}
.points-title{position:absolute;left:0;top:50px;width:846px;text-align:center;font-size:25px;font-weight:500;letter-spacing:.06em}
.points-title em{font-style:normal;color:var(--pink-deep);font-size:30px}
.points-title::before,.points-title::after{content:"";position:absolute;top:22px;width:130px;height:1px;background:var(--pink)}
.points-title::before{left:20px}
.points-title::after{right:20px}

.point-list{position:absolute;left:68px;top:115px;width:710px;display:flex;justify-content:space-between}
.point{width:210px;height:210px;border-radius:50%;background:var(--pink);color:var(--white);
  display:flex;flex-direction:column;align-items:center;padding-top:22px;text-align:center}
.point h3{font-size:16px;font-weight:500;letter-spacing:.1em;padding-bottom:7px;border-bottom:1px solid var(--white);width:130px;margin-bottom:10px;line-height:1.5}
.point p{font-size:16px;font-weight:700;line-height:1.35}
.point .big{font-size:28px;letter-spacing:.02em}
.point .small{font-size:8.5px;font-weight:400;margin-top:5px;line-height:1.4}

.contact{position:absolute;left:0;top:1000px;width:846px;height:200px;background:var(--grey)}
.contact-card{position:absolute;left:40px;top:30px;width:370px;height:140px;background:var(--white);text-align:center;padding-top:16px}
.contact-card .label{font-size:13px;letter-spacing:.2em;display:flex;align-items:center;justify-content:center;gap:10px}
.contact-card .label::before,.contact-card .label::after{content:"";width:60px;height:1px;background:var(--ink)}
.phone{font-family:"Montserrat",sans-serif;font-weight:500;font-size:44px;letter-spacing:.02em;line-height:1.3}
.contact-card .note{font-size:9.5px;line-height:1.5}
.venue{position:absolute;left:470px;top:48px;color:var(--white)}
.venue .name{font-family:"Noto Serif JP",serif;font-size:26px;font-weight:500;letter-spacing:.08em;margin-bottom:8px}
.venue p{font-size:13px;line-height:1.6}
.venue .fine{font-size:9px}
</style>
</head>
<body>
<main class="flyer">
  <section class="hero">
    <div class="hero-photo" role="img" aria-label="振袖姿の女性のポートレート写真"></div>
    <div class="deco a"></div>
    <div class="deco b"></div>
    <p class="collab">迎賓館 SAKURAGI × 二葉屋</p>
    <div class="kanji furi">振</div>
    <div class="kanji sode">袖</div>
    <p class="fair-title">special fair</p>
  </section>

  <div class="date-band">
    <span class="date">2023.2.1<span class="day">WED</span></span>
    <span class="arrow">▶▶</span>
    <span class="date">4.9<span class="day">SUN</span></span>
    <span class="times">①10:00〜 ②13:00〜</span>
  </div>
  <div class="time-notes"><span>ご予約優先</span><span>各回 2組限定</span></div>

  <section class="points">
    <h2 class="points-title">迎賓館 SAKURAGI の<em>3</em>つのおすすめポイント</h2>
    <div class="point-list">
      <div class="point">
        <h3>来館特典</h3>
        <p>ギフトカード<br><span class="big">3000円分</span><br>プレゼント!</p>
        <p class="small">※撮影予約の方に限ります<br>詳細はスタッフまで</p>
      </div>
      <div class="point">
        <h3>振 袖</h3>
        <p>【FURISODE No.1】<br>二葉屋カタログからの<br>衣裳の取り寄せも可能</p>
      </div>
      <div class="point">
        <h3>コーディネート</h3>
        <p>振袖に合わせた<br>ヘアメイク体験が<br>できちゃう!</p>
      </div>
    </div>
  </section>

  <footer class="contact">
    <div class="contact-card">
      <p class="label">ご予約・お問合せ</p>
      <p class="phone">025-123-4567</p>
      <p class="note">お電話またはメールにてお気軽にご予約ください。<br>ご予約の方を優先してご案内いたします。</p>
    </div>
    <div class="venue">
      <p class="name">迎賓館 SAKURAGI</p>
      <p>営業時間 / 10：00 〜 18：00</p>
      <p>Mail / info@sakuragi-photo.example</p>
      <p class="fine">【定休日 火曜・水曜日 ※祝日は営業】</p>
    </div>
  </footer>
</main>
</body>
</html>
```